Landing Page Only for text marketing service pingmo725.com

Our current site pingmo725.com needs a custom landing page for paid advertisements that is conversion centered as well as clear and concise. We want to focus on displaying the information effectively without getting too wordy or confusing to gain a higher conversion rate as our main goal.

We want more emphasis on the Try for $1 that includes 500 messages and custom keyword. The offer has no commitments. Upgrade or cancel at anytime.

We also want the landing page to focus on the benefits and marketing advantages (found in benefits tab), possible uses: mobile coupons, reminders/alerts, contests, daily specials, etc. (more examples can be found in how it works tab), and how it works.

The landing page can link to other parts of the site or use any information from other parts of the site. Our logo is attached in files. We want the design to match the overall color scheme of the site.

Target Market(s)

US based customers, business owners.

Industry/Entity Type

Marketing

Coding

Coded - Design and coding required

Number of Pages Required

1 page

Requirements
Must have
• See project description.
Nice to have
• See project description and any additional ideas welcomed from the designer.

```html
<!DOCTYPE html>
<html lang="en">
<head>
<meta charset="utf-8">
<title>Pingmo725 – SMS Messaging Platform</title>
<link href="https://fonts.googleapis.com/css2?family=Roboto:wght@300;400;500;700&display=swap" rel="stylesheet">
<style>
:root{
  --red:#d41f2b;
  --ink:#333333;
  --text:#444444;
  --muted:#666666;
  --band:#ececec;
  --white:#ffffff;
  --footer:#2b2b2b;
  --footer-text:#cfcfcf;
  --ring:#d6d6d6;
}
*{box-sizing:border-box;margin:0;padding:0}
html,body{width:1200px;height:3557px;overflow:hidden}
body{font-family:'Roboto',sans-serif;color:var(--text);background:var(--white);position:relative}
section,header,footer{position:absolute;left:0;width:1200px}
.abs{position:absolute}
.center{text-align:center}
.btn{position:absolute;background:var(--red);color:var(--white);display:flex;align-items:center;justify-content:center;border-radius:3px;font-weight:500;text-transform:uppercase}

/* header */
.topline{top:0;height:7px;background:#d9d9d9}
.site-header{top:7px;height:140px;background:var(--white)}
.logo{left:95px;top:44px;display:flex;align-items:center;gap:10px;font-size:34px;font-weight:500;color:var(--red)}
.logo-dot{width:22px;height:22px;border-radius:50%;background:var(--red)}
.contact-line{right:226px;top:28px;font-size:14px;color:var(--muted)}
.contact-line strong{font-size:20px;color:var(--ink);font-weight:500;margin-left:12px}
.login{left:1010px;top:17px;width:90px;height:38px;font-size:13px}
.nav{right:100px;top:78px;display:flex;height:41px}
.nav a{display:flex;align-items:center;padding:0 20px;font-size:13px;font-weight:500;color:var(--ink);text-decoration:none;text-transform:uppercase}
.nav a.active{background:#444;color:var(--white)}

/* hero */
.hero{top:147px;height:631px;background:linear-gradient(120deg,#2f2f31 0%,#5b5a5c 35%,#77706a 55%,#3a3a3c 100%)}
.hero-arrow{top:438px;width:48px;height:48px;border:2px solid rgba(255,255,255,.5);border-radius:50%;display:flex;align-items:center;justify-content:center}
.hero-title{right:100px;top:330px;text-align:right;color:var(--white);font-size:36px;font-weight:300;line-height:48px;text-transform:uppercase}
.hero-title b{color:var(--red);font-weight:700}
.hero-cta{left:925px;top:448px;width:175px;height:62px;font-size:22px}
.hero-sub{right:100px;top:552px;color:var(--white);font-size:21px;font-weight:500}

/* benefits */
.benefits{top:778px;height:515px}
.section-title{font-size:26px;font-weight:500;color:var(--ink);text-transform:uppercase;width:100%;text-align:center}
.benefits .section-title{top:44px}
.benefits-sub{top:88px;width:100%;text-align:center;font-size:21px;color:var(--muted)}
.benefit{width:300px;top:158px;text-align:center}
.benefit-ring{width:186px;height:186px;margin:0 auto;border-radius:50%;border:6px solid var(--ring);background:#3a3a3a;display:flex;align-items:center;justify-content:center}
.benefit-ring.hot{background:var(--red)}
.benefit h3{margin-top:38px;font-size:16px;font-weight:500;color:var(--ink);text-transform:uppercase}
.benefit p{margin:14px auto 0;width:260px;font-size:12px;line-height:16px;color:var(--muted)}

/* quote band */
.quote-band{top:1293px;height:154px;background:var(--band)}
.quote{left:100px;top:48px;width:560px;font-size:17px;line-height:28px;color:var(--ink)}
.call-btn{left:707px;top:42px;width:393px;height:67px;font-size:18px;text-transform:none;font-weight:400}
.call-btn strong{font-size:22px;font-weight:500;margin-left:8px}

/* how it works */
.how{top:1447px;height:493px}
.how .section-title{top:38px}
.how-media{left:100px;top:106px;width:498px;height:316px;border:4px solid #e3e3e3;background:linear-gradient(135deg,#5d6a78 0%,#98a4ae 45%,#c9d2d8 70%,#7c8690 100%)}
.steps{left:642px;top:107px;list-style:none}
.steps li{display:flex;align-items:center;height:43px;margin-bottom:25px;font-size:18px;font-weight:500;color:var(--ink)}
.steps span{width:43px;height:43px;border-radius:50%;background:#3a3a3a;color:var(--white);display:flex;align-items:center;justify-content:center;font-size:16px;margin-right:10px}

/* testimonials */
.clients-say{top:1940px;height:520px;background:var(--band)}
.side-arrow{top:92px}
.person{width:320px;top:57px;text-align:center}
.person-photo{width:184px;height:184px;margin:0 auto;border-radius:50%;border:6px solid #f4f4f4;box-shadow:0 0 0 1px #d0d0d0;background:linear-gradient(160deg,#cfcfcf,#8a8a8a)}
.person-photo.color{background:linear-gradient(160deg,#8fb9e6,#5a6f8a 60%,#2d3540)}
.person h4{margin-top:42px;font-size:18px;font-weight:400;color:var(--ink);line-height:26px}
.trial-btn{left:439px;top:380px;width:322px;height:59px;font-size:20px}
.trial-note{top:457px;width:100%;text-align:center;font-size:18px;color:var(--muted)}

/* features */
.features{top:2460px;height:554px}
.features .section-title{top:48px}
.feature{width:260px;top:132px;text-align:center}
.feature-ring{width:114px;height:114px;margin:0 auto;border-radius:50%;border:2px solid #cfcfcf;display:flex;align-items:center;justify-content:center}
.feature h3{margin-top:38px;font-size:17px;font-weight:500;color:var(--ink);text-transform:uppercase}
.try-btn{left:491px;top:362px;width:218px;height:62px;font-size:26px}
.features-copy{top:450px;left:150px;width:900px;text-align:center;font-size:18px;line-height:29px;color:var(--muted)}

/* client names */
.client-band{top:3014px;height:204px;background:var(--band)}
.client-band .section-title{top:38px}
.client-row{top:104px;left:0;width:1200px;display:flex;justify-content:center;gap:120px}
.client-name{font-size:36px;font-weight:500;color:#777;display:flex;align-items:center;gap:12px}
.client-mark{width:14px;height:14px;background:#777;border-radius:50%}

/* footer */
.site-footer{top:3218px;height:339px;background:var(--footer);color:var(--footer-text)}
.footer-col{top:56px}
.footer-col h5{font-size:22px;font-weight:400;color:var(--white);margin-bottom:16px}
.footer-col li{list-style:none;font-size:12px;line-height:25px}
.newsletter p{font-size:12px;line-height:22px;width:290px}
.news-form{display:flex;margin-top:14px}
.news-input{width:200px;height:38px;border:1px solid #777;font-size:11px;color:#999;display:flex;align-items:center;padding-left:10px}
.news-go{width:46px;height:38px;margin-left:4px;background:var(--red);color:var(--white);font-size:13px;font-weight:500;display:flex;align-items:center;justify-content:center}
.social li{display:flex;align-items:center;gap:12px}
.social li i{width:11px;height:11px;border-radius:50%;background:var(--footer-text);display:inline-block}
.copyright{top:284px;width:100%;text-align:center;font-size:12px}
</style>
</head>
<body>

<div class="abs topline" style="left:0;width:1200px"></div>

<header class="site-header">
  <div class="abs logo"><span class="logo-dot"></span>Pingmo725</div>
  <div class="abs contact-line">Questions? Contact the team <strong>1-800-555-0142</strong></div>
  <a class="btn login">
    <svg width="12" height="12" viewBox="0 0 12 12" style="margin-right:6px"><circle cx="6" cy="4" r="3" fill="#fff"/><path d="M0 12c0-4 12-4 12 0z" fill="#fff"/></svg>Login
  </a>
  <nav class="abs nav">
    <a class="active">Pricing</a><a>Benefits</a><a>How it works</a><a>Resellers</a><a>Sign up</a>
  </nav>
</header>

<section class="hero" role="img" aria-label="Photo of hands holding a smartphone and typing a text message">
  <div class="abs hero-arrow" style="left:35px">
    <svg width="14" height="20" viewBox="0 0 14 20"><path d="M11 2 3 10l8 8" stroke="#fff" stroke-width="2" fill="none" opacity=".7"/></svg>
  </div>
  <div class="abs hero-arrow" style="left:1117px">
    <svg width="14" height="20" viewBox="0 0 14 20"><path d="M3 2l8 8-8 8" stroke="#fff" stroke-width="2" fill="none" opacity=".7"/></svg>
  </div>
  <h1 class="abs hero-title">The most <b>cost-effective</b><br>SMS messaging platform</h1>
  <a class="btn hero-cta">Try for $1</a>
  <p class="abs hero-sub">that includes 500 messages and custom keyworda</p>
</section>

<section class="benefits">
  <h2 class="abs section-title">Our Benefits</h2>
  <p class="abs benefits-sub">Did you know over 83% of texts are read within an hour?</p>

  <div class="abs benefit" style="left:85px">
    <div class="benefit-ring">
      <svg width="84" height="60" viewBox="0 0 84 60" fill="none" stroke="#fff" stroke-width="3">
        <rect x="14" y="4" width="66" height="36" rx="2"/>
        <path d="M4 16v38h66"/>
        <circle cx="47" cy="22" r="9"/>
        <text x="47" y="27" fill="#fff" stroke="none" font-size="14" font-family="Roboto,sans-serif" text-anchor="middle">$</text>
      </svg>
    </div>
    <h3>Increase revenue</h3>
    <p>There are many variations of passages of Lorem Ipsum available, but the majority have suffered alteration in some</p>
  </div>

  <div class="abs benefit" style="left:450px">
    <div class="benefit-ring hot">
      <svg width="80" height="70" viewBox="0 0 80 70" fill="none" stroke="#fff" stroke-width="3">
        <path d="M40 6v54M22 60h36M12 16h56"/>
        <path d="M12 16 2 40h20zM68 16 58 40h20z"/>
        <path d="M2 40a10 6 0 0 0 20 0M58 40a10 6 0 0 0 20 0"/>
      </svg>
    </div>
    <h3>Lift your workload</h3>
    <p>There are many variations of passages of Lorem Ipsum available, but the majority have suffered alteration in some</p>
  </div>

  <div class="abs benefit" style="left:815px">
    <div class="benefit-ring">
      <svg width="76" height="76" viewBox="0 0 76 76" fill="none" stroke="#fff" stroke-width="3">
        <circle cx="32" cy="44" r="26"/>
        <path d="M32 28v16h12"/>
        <circle cx="54" cy="20" r="15" fill="#3a3a3a"/>
        <text x="54" y="26" fill="#fff" stroke="none" font-size="17" font-family="Roboto,sans-serif" text-anchor="middle">$</text>
      </svg>
    </div>
    <h3>Save time</h3>
    <p>There are many variations of passages of Lorem Ipsum available, but the majority have suffered alteration in some</p>
  </div>
</section>

<section class="quote-band">
  <p class="abs quote">"I switched suppliers &amp; now have Pingmo725. Training, support, &amp; functionality are superb. This will be a long term relationship."</p>
  <a class="btn call-btn">Questions? Give us a call. <strong>1-800-555-0142</strong></a>
</section>

<section class="how">
  <h2 class="abs section-title">How it works</h2>
  <div class="abs how-media" role="img" aria-label="Photo of a businessman holding a phone with envelope icons flying out of the screen"></div>
  <ol class="abs steps">
    <li><span>1</span>Sign-Up For Your Keyword</li>
    <li><span>2</span>Promote Your Keyword</li>
    <li><span>3</span>Customers/Leads Opt-In</li>
    <li><span>4</span>Send Out Your Group Text Message</li>
    <li><span>5</span>Reap Your Rewards</li>
  </ol>
</section>

<section class="clients-say">
  <svg class="abs side-arrow" style="left:55px" width="36" height="110" viewBox="0 0 36 110"><path d="M34 2 2 55l32 53" stroke="#cfcfcf" stroke-width="2" fill="none"/></svg>
  <svg class="abs side-arrow" style="left:1110px" width="36" height="110" viewBox="0 0 36 110"><path d="M2 2l32 53L2 108" stroke="#cfcfcf" stroke-width="2" fill="none"/></svg>

  <div class="abs person" style="left:75px">
    <div class="person-photo color" role="img" aria-label="Portrait photo of a smiling business owner in a suit"></div>
    <h4>Harold M., Owner<br>Brightline Marketing</h4>
  </div>
  <div class="abs person" style="left:440px">
    <div class="person-photo" role="img" aria-label="Black and white portrait photo of a vice president with glasses"></div>
    <h4>Derek S., VP<br>Northwave Radio</h4>
  </div>
  <div class="abs person" style="left:805px">
    <div class="person-photo" role="img" aria-label="Black and white portrait photo of a smiling chief executive"></div>
    <h4>Laura K., CEO<br>Summit Ridge Real Estate</h4>
  </div>

  <a class="btn trial-btn">Try your first month for $1</a>
  <p class="abs trial-note">Only $19.95/month afterwards</p>
</section>

<section class="features">
  <h2 class="abs section-title">Features at a glance</h2>

  <div class="abs feature" style="left:62px">
    <div class="feature-ring">
      <svg width="40" height="28" viewBox="0 0 40 28"><rect x="1" y="1" width="38" height="26" fill="#333"/><path d="M1 1l19 15L39 1" stroke="#fff" stroke-width="2" fill="none"/></svg>
    </div>
    <h3>Send bulk messages</h3>
  </div>

  <div class="abs feature" style="left:337px">
    <div class="feature-ring">
      <svg width="46" height="46" viewBox="0 0 46 46" fill="#333" stroke="#333" stroke-width="2">
        <circle cx="23" cy="14" r="6"/><path d="M14 30c0-10 18-10 18 0z"/>
        <path d="M23 30v6M14 30l-8 8M32 30l8 8" fill="none"/>
        <circle cx="6" cy="40" r="3"/><circle cx="23" cy="40" r="3"/><circle cx="40" cy="40" r="3"/>
      </svg>
    </div>
    <h3>Unlimited subscribers</h3>
  </div>

  <div class="abs feature" style="left:615px">
    <div class="feature-ring">
      <svg width="40" height="40" viewBox="0 0 40 40">
        <rect x="2" y="6" width="36" height="32" rx="2" fill="none" stroke="#333" stroke-width="3"/>
        <rect x="2" y="6" width="36" height="8" fill="#333"/>
        <path d="M11 2v8M29 2v8" stroke="#333" stroke-width="3"/>
        <g fill="#333"><rect x="8" y="18" width="5" height="4"/><rect x="17" y="18" width="5" height="4"/><rect x="26" y="18" width="5" height="4"/><rect x="8" y="27" width="5" height="4"/><rect x="17" y="27" width="5" height="4"/><rect x="26" y="27" width="5" height="4"/></g>
      </svg>
    </div>
    <h3>Schedule messages</h3>
  </div>

  <div class="abs feature" style="left:892px">
    <div class="feature-ring">
      <svg width="42" height="42" viewBox="0 0 42 42" fill="none" stroke="#333" stroke-width="3"><circle cx="21" cy="21" r="18"/><path d="M21 10v11h8"/></svg>
    </div>
    <h3>Auto-responder</h3>
  </div>

  <a class="btn try-btn">Try for $1</a>
  <p class="abs features-copy">Features so jam packed we could only list four. You ready to signup yet? Start sending messages, adding subscribers and scheduling in minutes. Plus what if we told you there's a bunch more under the hood?</p>
</section>

<section class="client-band">
  <h2 class="abs section-title">Satisfied clients</h2>
  <div class="abs client-row">
    <span class="client-name">Burgerly</span>
    <span class="client-name">Sandwichco</span>
    <span class="client-name">Provista</span>
    <span class="client-name">Fizzmark</span>
  </div>
</section>

<footer class="site-footer">
  <div class="abs footer-col" style="left:100px">
    <h5>How To Use</h5>
    <ul><li>How it Works</li><li>Videos</li><li>FAQs</li><li>Support</li></ul>
  </div>
  <div class="abs footer-col" style="left:277px">
    <h5>Company</h5>
    <ul><li>About</li><li>Benefits</li><li>Resellers</li><li>Sign Up</li><li>Login</li><li>Affiliate</li><li>Blog</li></ul>
  </div>
  <div class="abs footer-col" style="left:441px">
    <h5>Contact US</h5>
    <ul><li>Maple Court, Suite 210</li><li>42 Orchard Lane, Springfield 4021</li><li>info@pingmo725.com</li><li>+1 (555) 014 2290</li></ul>
  </div>
  <div class="abs footer-col newsletter" style="left:673px">
    <h5>Newsletter</h5>
    <p>Dolore magnam aliquam quaerat voluptatem. Ut enim blanditiis praesentium voluptatum</p>
    <div class="news-form"><div class="news-input">Enter Your Email</div><div class="news-go">GO !</div></div>
  </div>
  <div class="abs footer-col social" style="left:1003px">
    <h5>Follow Us</h5>
    <ul><li><i></i>pagewall</li><li><i></i>chirpline</li><li><i></i>snapgrid</li><li><i></i>circleplus</li></ul>
  </div>
  <p class="abs copyright">@ Copy Rights -2016 © Pingmo725. All rights reserved.</p>
</footer>

</body>
</html>
```